Fairway Relief Rockets promotional cards (rack card)

This will be an eye catching (rack) card designed to be left at the Golf clubhouse with special event coordinators and emailed or physically handed to charities conducting fund raising golf tournaments. I need an electronic file version that I could email to prospects to view before they decide if they will help promote this to their tournament directors
Photos, logos, files and website link are attached. all photos on my website are available upon request.
www.fairwayreliefrockets.com
Target Market(s)
must be appealing to charities conducting golf tournaments as a method to raise funds,
Industry/Entity Type
Golf Course
Font styles to use
Other font styles liked:
- Screwed Oblique for any bold type, serif for body text
Requirements
Must have
- include a call to action to "book your event now"
- use the colors in my logo
- include the photo attached, could include additional photos from my website
- include "several packages to choose from"
- I would like this to be vectorized to be able to resize or shrink slightly as needed to fit printables.
Nice to have
- in the background of photos, there is a 7 foot pull up banner that participants often stand in front of to take videos and photos, you can incorporate that if possible as a watermark or background image. I can provide that original image if needed.
Should not have
- any salesy "car commercial" banners or balloons or stars or anything like that.

```html
<!DOCTYPE html>
<html lang="en">
<head>
<meta charset="utf-8">
<title>Fairway Relief Rockets – Rack Card</title>
<link href="https://fonts.googleapis.com/css2?family=Josefin+Sans:wght@400;600;700&family=Open+Sans:wght@400;600&display=swap" rel="stylesheet">
<style>
  :root{
    --teal:#14967a;
    --teal-dark:#0f7d66;
    --forest:#0d5a2e;
    --yellow:#f3e36a;
    --pale-yellow:#efe59a;
    --card:#f1f1f1;
    --card-shade:#dedede;
    --ink:#1c1c1c;
    --rule:#8a8a8a;
    --page:#e6e6e6;
    --photo-sky:#5f7a4a;
    --photo-grass:#4f8a3a;
  }
  *{box-sizing:border-box;margin:0;padding:0}
  html,body{width:1200px;height:1200px;overflow:hidden;background:var(--page)}
  body{position:relative;font-family:"Open Sans",Arial,sans-serif;color:var(--ink)}
  .card{position:absolute;left:195px;width:810px;height:540px;overflow:hidden;
        background:linear-gradient(160deg,#fafafa 0%,var(--card) 55%,var(--card-shade) 100%);
        box-shadow:0 6px 18px rgba(0,0,0,.25)}
  .card--front{top:40px}
  .card--back{top:620px}
  .card svg.shapes{position:absolute;inset:0}
  .abs{position:absolute}

  /* front */
  .brand{left:22px;top:50px;width:340px;padding:10px 0 8px;border-top:2px solid var(--teal);border-bottom:2px solid var(--teal);white-space:nowrap}
  .brand__name{font-family:"Josefin Sans",Arial,sans-serif;font-weight:700;font-size:22px;color:var(--forest);letter-spacing:.3px;text-transform:uppercase}
  .headline{left:34px;top:142px;width:400px;font-family:"Josefin Sans",Arial,sans-serif;font-weight:600;color:#fff;font-size:24px;line-height:37px;letter-spacing:1.5px;text-transform:uppercase}
  .headline__answer{left:34px;top:294px;font-family:"Josefin Sans",Arial,sans-serif;font-weight:700;color:var(--yellow);font-size:26px;letter-spacing:1.5px}
  .lede{left:34px;top:338px;width:360px;font-family:"Josefin Sans",Arial,sans-serif;color:#fff;font-size:16px;line-height:25px;letter-spacing:.6px}
  .photo{left:0;top:0}
  .intro{left:36px;top:442px;width:380px;font-size:15px;line-height:24px}
  .cta{left:560px;top:440px;width:245px;text-align:center}
  .cta__rule{height:2px;background:#fff;width:160px;margin:0 auto 9px}
  .cta__title{font-family:"Josefin Sans",Arial,sans-serif;font-weight:700;color:var(--yellow);font-size:15px;letter-spacing:1.5px;white-space:nowrap}
  .cta__web{color:#fff;font-size:10.5px;margin:5px 0;letter-spacing:.3px}
  .cta__phone{font-family:"Josefin Sans",Arial,sans-serif;font-weight:700;color:var(--yellow);font-size:17px;letter-spacing:1px;display:inline-block;border-bottom:2px solid #fff;padding-bottom:3px;white-space:nowrap}

  /* back */
  .pitch{left:40px;top:0;width:340px;height:195px;background:var(--teal);color:#fff;font-size:13px;line-height:28px;text-align:center;padding:14px 16px}
  .packages__title{left:52px;top:204px;font-size:15px;letter-spacing:.8px;color:var(--ink)}
  .packages{left:20px;top:234px;width:320px;border:1px solid var(--teal)}
  .pkg{position:relative;height:54px;border-top:1px solid var(--teal);text-align:center;color:var(--teal-dark);font-size:9.5px;line-height:14px;padding:17px 10px 0}
  .pkg:first-child{border-top:0}
  .pkg--alt{background:var(--pale-yellow)}
  .pkg__tag{position:absolute;left:50%;top:0;transform:translateX(-50%);background:var(--teal);color:#fff;font-size:9px;letter-spacing:2px;padding:1px 18px;line-height:13px}
  .contact{left:0;top:462px;width:355px;height:78px;background:var(--teal);color:#fff;font-size:10px;line-height:19px;text-align:center;padding-top:10px}
  .stamp{left:650px;top:44px;width:130px;height:130px;border:1px solid #666}
  .address-line{left:420px;width:360px;height:1px;background:var(--rule)}
</style>
</head>
<body>

<section class="card card--front" aria-label="Rack card front">
  <svg class="shapes" width="810" height="540" viewBox="0 0 810 540" aria-hidden="true">
    <polygon points="600,30 810,30 810,130 585,130" fill="var(--teal)"/>
    <polygon points="0,135 470,135 430,410 0,410" fill="var(--teal)"/>
    <polygon points="550,430 810,430 810,540 530,540" fill="var(--teal)"/>
    <line x1="445" y1="420" x2="810" y2="420" stroke="#fff" stroke-width="3"/>
  </svg>
  <svg class="abs photo" width="810" height="540" viewBox="0 0 810 540" role="img" aria-label="Photo: a participant in ear protection fires the golf ball launcher on a tournament fairway beside a pull-up banner">
    <defs>
      <linearGradient id="photoTone" x1="0" y1="0" x2="0" y2="1">
        <stop offset="0" stop-color="var(--photo-sky)"/>
        <stop offset="1" stop-color="var(--photo-grass)"/>
      </linearGradient>
    </defs>
    <polygon points="478,135 810,135 810,410 440,410" fill="url(#photoTone)"/>
  </svg>

  <div class="abs brand"><span class="brand__name">Fairway Relief Rockets</span></div>

  <h1 class="abs headline">Tired and bored of the same old challenges at every charity golf tournament?</h1>
  <p class="abs headline__answer">WELL, NOT ANYMORE!</p>
  <p class="abs lede">How about this exciting alternative for your fundraising efforts!</p>

  <p class="abs intro">At Fairway Relief Rockets, We provide you with an RX&#8209;15 GOLF BALL LAUNCHER plus it comes with a prize for closest to the 400 yard target!</p>

  <div class="abs cta">
    <div class="cta__rule"></div>
    <p class="cta__title">BOOK YOUR EVENT NOW</p>
    <p class="cta__web">www.fairwayreliefrockets.com</p>
    <p class="cta__phone">Or Call 555-014-2290</p>
  </div>
</section>

<section class="card card--back" aria-label="Rack card back">
  <p class="abs pitch">We have several package options to choose from that are guaranteed to make your golf event a memorable one! Your players will be talking about this one all day long! It is completely SAFE, FUN and an experience that ALL AGES can participate in.</p>

  <h2 class="abs packages__title">PACKAGES AVAILABLE INCLUDE:</h2>

  <div class="abs packages">
    <div class="pkg"><span class="pkg__tag">OPTION 1</span>($250 fee) $5 or $10 per player/per shot<br>(player pays to participate) ( player provides a ball)</div>
    <div class="pkg pkg--alt"><span class="pkg__tag">OPTION 2</span>($500 fee -sponsor level) $5 or $10 per player/per shot and I provide all players a logo ball) 100% profit to the charity</div>
    <div class="pkg"><span class="pkg__tag">OPTION 3</span>($500 fee -sponsor level) player participation is included in mulligan package price. 100% profit to the charity</div>
    <div class="pkg pkg--alt"><span class="pkg__tag">OPTION 4</span><br>Custom package design based upon charity requests</div>
  </div>

  <div class="abs contact">
    For more info or book your date, contact us via:<br>
    dana@fairwayreliefrockets.com<br>
    Phone : 555-014-2290 &nbsp;|&nbsp; www.fairwayreliefrockets.com
  </div>

  <div class="abs stamp" aria-label="Stamp area"></div>
  <div class="abs address-line" style="top:250px"></div>
  <div class="abs address-line" style="top:300px"></div>
  <div class="abs address-line" style="top:350px"></div>
  <div class="abs address-line" style="top:400px"></div>
</section>

</body>
</html>
```